International online gaming platform needs a game UI design

1. We need a game interface for three kinds of theme based on our guideline and sample mockup.
2. The product type is the online casino games related, we need a series of casino games UIs, however, we can start on the game lobby first.
3. Three theme you might choose from or refer to:
A. 3D look & feel
B. Realistic casino theme
C. Richness and grandeur
D. European casino style
4. NOT ALLOWED to change the design layout.
MUST follow our sample mock up and ONLY redefine the design style.
5. All items must be in a stand-alone component, eg. Button, Tab, Icon,... etc.
6. We need the layout in vector shape, but we can review in JPG or PNG format.
7. The image size: 1366 x 768

Updated:
1. All items and their positions should be same as the sample UI we provided.
Please redesign all the items and create a new theme for it.
No need to create a new layout.
2. Although we accept the draft design, but all the items in UI should be completed.
3. All the wordings in the sample UI are confirmed, you might change the fonts.
4. For the avatar in the left hand side, you don't have to redraw it.
We already have our own avatar system implemented.
5. All the items such as icons, tabs, and buttons are free to redesign.

Dear designers,

We've increased our budget and raise the prize money to 800 USD.  
We also accept the draft design in PNG format and we can go through the details in handover stage.
Thank you very much. 

Reason: Dear designers, We decided to extend the deadline by 7 days. As mentioned in the task description, we are looking for a new style of design and you might refer to the below style. A. 3D look & feel B. Realistic casino theme C. Richness and grandeur D. European casino style If you are still interested in our project, please send us your work. Thank you very much!

Casino

```html
<!DOCTYPE html>
<html lang="en">
<head>
<meta charset="utf-8">
<title>Live Casino Lobby</title>
<link rel="stylesheet" href="https://fonts.googleapis.com/css2?family=Signika:wght@400;600;700&family=Roboto+Condensed:wght@400;700&display=swap">
<style>
:root{
  --page:#f4f4f6;
  --navy-deep:#07092a;
  --navy:#0d1445;
  --navy-mid:#1a2470;
  --navy-light:#2b3a9a;
  --edge:#5b6bc9;
  --line:#c9d0f5;
  --white:#ffffff;
  --text-soft:#cfd5f7;
  --felt:#0f4a4a;
  --felt-light:#1b6a66;
  --felt-line:#d9e8c8;
  --gold:#e6c657;
  --gold-dark:#b58a1f;
  --red:#c8202c;
  --blue:#2a3fa8;
  --grid:#cfd3e2;
}
*{box-sizing:border-box;margin:0;padding:0}
html,body{width:1200px;height:1000px;overflow:hidden;background:var(--page)}
body{font-family:"Roboto Condensed",Arial,sans-serif;color:var(--white);position:relative}
.lobby{position:absolute;left:0;top:156px;width:1200px;height:688px;background:linear-gradient(180deg,var(--navy) 0%,var(--navy-deep) 100%);overflow:hidden}
.topbar{position:absolute;left:0;top:0;width:1200px;height:40px;background:var(--navy-deep);border-bottom:2px solid var(--line)}
.topbar-stripes{position:absolute;left:230px;top:0;width:780px;height:38px;background:repeating-linear-gradient(90deg,var(--navy-light) 0 2px,transparent 2px 7px);opacity:.55}
.brand{position:absolute;left:10px;top:6px;display:flex;align-items:center;gap:10px}
.brand-dot{width:26px;height:26px;border-radius:50%;background:var(--white)}
.brand-name{font-family:"Signika",sans-serif;font-weight:700;font-size:26px;letter-spacing:.5px;color:var(--white)}
.window-controls{position:absolute;right:12px;top:7px;display:flex;gap:6px}
.ctrl{width:28px;height:26px;border-radius:4px;background:linear-gradient(#fff,#cfd2dc);display:flex;align-items:center;justify-content:center;color:var(--navy-deep);font-weight:700;font-size:15px}
.ctrl.close{color:var(--red)}
.sidebar{position:absolute;left:0;top:40px;width:184px;height:598px;border-right:2px solid var(--line);background:linear-gradient(90deg,var(--navy-deep),var(--navy))}
.clock{position:absolute;left:8px;top:18px;width:168px;height:22px;background:var(--navy-deep);border:1px solid var(--edge);border-radius:3px;font-size:11px;line-height:20px;text-align:center;color:var(--text-soft)}
.avatar-frame{position:absolute;left:12px;top:56px;width:160px;height:212px;border:2px solid var(--navy-light);border-radius:4px;background:var(--navy-mid);padding:6px}
.avatar-art{width:144px;height:164px;background:linear-gradient(180deg,#3a7fb2,#1b3d6a);border:1px solid var(--edge)}
.username{margin-top:8px;text-align:center;font-size:12px;color:var(--text-soft)}
.side-btn{position:absolute;left:22px;width:140px;height:26px;border-radius:3px;background:linear-gradient(180deg,var(--navy-light),var(--navy-deep));border-top:1px solid var(--edge);font-size:11px;font-weight:700;text-align:center;line-height:25px;letter-spacing:.3px}
.side-btn.profile{top:272px;font-size:13px;background:var(--navy-deep);border:1px solid var(--edge)}
.side-btn.announcements{top:326px}
.side-btn.rules{top:368px}
.side-btn.tour{top:410px}
.coins-art{position:absolute;left:58px;top:468px;width:67px;height:86px;border-radius:40%;background:radial-gradient(circle,#f1d56b,var(--gold-dark))}
.main{position:absolute;left:188px;top:40px;width:1008px;height:598px}
.game-tab{position:absolute;top:10px;height:40px;display:flex;align-items:center;justify-content:center;gap:10px;font-family:"Signika",sans-serif;font-weight:600;font-size:21px;background:linear-gradient(180deg,var(--navy-mid),var(--navy-deep));border-radius:6px 6px 0 0}
.game-tab.active{font-size:24px;background:linear-gradient(180deg,var(--navy-light),var(--navy-mid));border:1px solid var(--edge);border-bottom:none}
.dealer-strip{position:absolute;left:0;top:50px;width:1008px;height:140px;border-bottom:2px solid var(--edge)}
.dealer-card{position:absolute;top:10px;display:flex;flex-direction:column}
.dealer-card.featured{left:20px;top:5px;width:277px;height:128px;padding:8px 10px;background:var(--navy-mid);border:1px solid var(--edge);border-radius:4px}
.dealer-media{display:flex;gap:8px}
.dealer-photo{background:linear-gradient(180deg,#3d4d6e,#141c33);border:1px solid var(--edge)}
.roadmap{background:var(--white)}
.dealer-meta{display:flex;justify-content:space-between;font-size:11px;font-weight:700;margin-top:10px}
.deals-badge{background:var(--red);border:1px solid var(--white);padding:0 5px;border-radius:2px}
.multiplayer-tab{position:absolute;left:20px;top:198px;width:147px;height:33px;border-radius:5px 5px 0 0;background:var(--navy-mid);border:1px solid var(--edge);border-bottom:none;font-size:14px;font-weight:700;display:flex;align-items:center;gap:8px;padding-left:14px}
.limit-filter{position:absolute;left:474px;top:205px;width:508px;height:30px;border:1px solid var(--edge);border-radius:4px;background:var(--navy-deep);display:flex;font-size:13px;font-weight:700}
.limit-filter span{border-right:1px solid var(--edge);display:flex;align-items:center;justify-content:center;flex:0 0 52px}
.limit-filter .join-any{flex:0 0 110px}
.limit-filter .all-limits{flex:1;border-right:none;justify-content:flex-end;padding-right:12px}
.table-panel{position:absolute;left:17px;top:240px;width:982px;height:350px;border:1px solid var(--edge);border-radius:4px;background:rgba(5,8,35,.6)}
.table-card{position:absolute;width:302px;height:148px;border:3px solid var(--line);border-radius:5px;background:linear-gradient(180deg,var(--navy-deep),#101a3d);padding:6px 10px;overflow:hidden}
.table-head{display:flex;justify-content:space-between;font-size:12px;font-weight:700;line-height:15px}
.join-btn{position:absolute;left:78px;top:12px;width:145px;height:46px;border-radius:50%;background:linear-gradient(180deg,var(--navy-light) 0%,var(--navy-mid) 45%,var(--navy-deep) 100%);border:3px solid var(--white);box-shadow:0 0 6px rgba(201,208,245,.5);display:flex;align-items:center;justify-content:center;font-family:"Signika",sans-serif;font-weight:700;font-style:italic;font-size:24px;color:var(--white);z-index:2}
.felt{position:absolute;left:8px;right:8px;top:60px;bottom:6px;background:linear-gradient(180deg,var(--felt-light),var(--felt));display:grid;grid-template-columns:repeat(8,1fr);grid-template-rows:1fr 1fr;border-top:2px solid var(--felt-line)}
.felt i{font-style:italic;font-weight:700;font-size:12px;display:flex;align-items:center;justify-content:center;border-right:1px solid var(--felt-line);border-bottom:1px solid var(--felt-line)}
.felt i.b{color:var(--gold)}
.felt i.p{color:var(--white)}
.scroll-track{position:absolute;left:983px;top:255px;width:18px;height:305px;border-radius:3px;background:var(--navy-deep);border:1px solid var(--edge)}
.scroll-thumb{width:16px;height:30px;background:linear-gradient(180deg,#b8a7e6,var(--navy-light));border-radius:3px}
.footer{position:absolute;left:0;top:638px;width:1200px;height:50px;border-top:2px solid var(--line);background:linear-gradient(180deg,var(--navy),var(--navy-deep))}
.balance{position:absolute;left:928px;top:4px;width:267px;height:32px;display:flex;font-size:14px;font-weight:700;border-radius:3px;overflow:hidden;border:1px solid var(--white)}
.balance-label{background:var(--red);width:78px;display:flex;align-items:center;justify-content:center}
.balance-currency{background:var(--white);color:var(--navy-deep);width:55px;display:flex;align-items:center;justify-content:center;border-right:1px solid var(--grid)}
.balance-value{background:#e9ebf2;color:var(--navy-deep);flex:1;display:flex;align-items:center;justify-content:center}
</style>
</head>
<body>
<main class="lobby">
  <header class="topbar">
    <div class="topbar-stripes"></div>
    <div class="brand"><span class="brand-dot"></span><span class="brand-name">LIVE CASINO</span></div>
    <div class="window-controls">
      <span class="ctrl">$</span>
      <span class="ctrl"><svg width="16" height="16" viewBox="0 0 16 16"><circle cx="7" cy="7" r="5" fill="none" stroke="#07092a" stroke-width="2"/><line x1="11" y1="11" x2="15" y2="15" stroke="#07092a" stroke-width="2"/></svg></span>
      <span class="ctrl"></span>
      <span class="ctrl"></span>
      <span class="ctrl close">✕</span>
    </div>
  </header>

  <aside class="sidebar">
    <div class="clock">1/28/2014 06:54 PM GMT + 8</div>
    <div class="avatar-frame">
      <div class="avatar-art" role="img" aria-label="Player avatar"></div>
      <div class="username">ALPos848767</div>
    </div>
    <div class="side-btn profile">PROFILE</div>
    <div class="side-btn announcements">ANNOUNCEMENTS</div>
    <div class="side-btn rules">RULES &amp; REGULATION</div>
    <div class="side-btn tour">QUICK TOUR</div>
    <div class="coins-art" role="img" aria-label="Pile of gold casino coins"></div>
  </aside>

  <section class="main">
    <div class="game-tab active" style="left:5px;width:233px">
      <svg width="24" height="24" viewBox="0 0 24 24"><rect x="2" y="4" width="12" height="17" rx="2" fill="#fff" transform="rotate(-12 8 12)"/><rect x="9" y="3" width="12" height="17" rx="2" fill="#fff" stroke="#0d1445"/></svg>BACARAT</div>
    <div class="game-tab" style="left:242px;width:233px">
      <svg width="20" height="20" viewBox="0 0 20 20"><rect x="1" y="1" width="9" height="9" rx="2" fill="#c8202c"/><rect x="9" y="9" width="10" height="10" rx="2" fill="#e04040"/></svg>SUPER SIX</div>
    <div class="game-tab" style="left:479px;width:238px">
      <svg width="22" height="22" viewBox="0 0 22 22"><circle cx="11" cy="11" r="10" fill="#b58a1f"/><circle cx="11" cy="11" r="5" fill="#e6c657"/></svg>ROULETTE</div>
    <div class="game-tab" style="left:720px;width:217px">
      <svg width="22" height="20" viewBox="0 0 22 20"><rect x="1" y="6" width="10" height="10" rx="2" fill="#c8202c"/><rect x="10" y="2" width="10" height="10" rx="2" fill="#e04040"/></svg>SIC BO</div>

    <div class="dealer-strip">
      <div class="dealer-card featured">
        <div class="dealer-media">
          <div class="dealer-photo" role="img" aria-label="Dealer portrait" style="width:78px;height:78px"></div>
          <svg class="roadmap" width="168" height="78" viewBox="0 0 168 78">
            <g stroke="#cfd3e2" stroke-width="1">
              <path d="M14 0V78M28 0V78M42 0V78M56 0V78M70 0V78M84 0V78M98 0V78M112 0V78M126 0V78M140 0V78M154 0V78M0 13H168M0 26H168M0 39H168M0 52H168M0 65H168"/>
            </g>
            <g fill="none" stroke-width="2">
              <circle cx="7" cy="6.5" r="4.5" stroke="#2a3fa8"/><circle cx="7" cy="19.5" r="4.5" stroke="#2a3fa8"/>
              <circle cx="21" cy="6.5" r="4.5" stroke="#c8202c"/><circle cx="35" cy="6.5" r="4.5" stroke="#2a3fa8"/>
              <circle cx="49" cy="6.5" r="4.5" stroke="#c8202c"/><circle cx="63" cy="6.5" r="4.5" stroke="#2a3fa8"/>
              <circle cx="77" cy="6.5" r="4.5" stroke="#c8202c"/><circle cx="91" cy="6.5" r="4.5" stroke="#2a3fa8"/>
              <circle cx="119" cy="6.5" r="4.5" stroke="#2a3fa8"/><circle cx="119" cy="19.5" r="4.5" stroke="#2a3fa8"/>
              <circle cx="133" cy="6.5" r="4.5" stroke="#c8202c"/><circle cx="133" cy="19.5" r="4.5" stroke="#c8202c"/>
              <circle cx="133" cy="32.5" r="4.5" stroke="#c8202c"/><circle cx="133" cy="45.5" r="4.5" stroke="#c8202c"/>
              <circle cx="133" cy="58.5" r="4.5" stroke="#c8202c"/><circle cx="147" cy="6.5" r="4.5" stroke="#c8202c"/>
            </g>
          </svg>
        </div>
        <div class="dealer-meta" style="margin-top:8px"><span>Dealer Name</span><span class="deals-badge">Deals 999</span></div>
      </div>

      <div class="dealer-card" style="left:320px;width:213px">
        <div class="dealer-media">
          <div class="dealer-photo" role="img" aria-label="Dealer portrait" style="width:70px;height:66px"></div>
          <svg class="roadmap" width="135" height="66" viewBox="0 0 135 66"><g stroke="#cfd3e2"><path d="M13.5 0V66M27 0V66M40.5 0V66M54 0V66M67.5 0V66M81 0V66M94.5 0V66M108 0V66M121.5 0V66M0 13H135M0 26H135M0 39H135M0 52H135"/></g><g fill="none" stroke-width="2"><circle cx="7" cy="6.5" r="4.5" stroke="#2a3fa8"/><circle cx="7" cy="19.5" r="4.5" stroke="#c8202c"/><circle cx="20" cy="6.5" r="4.5" stroke="#c8202c"/><circle cx="34" cy="6.5" r="4.5" stroke="#c8202c"/><circle cx="47" cy="6.5" r="4.5" stroke="#2a3fa8"/></g></svg>
        </div>
        <div class="dealer-meta"><span>Dealer Name</span><span>Deals 999</span></div>
      </div>
      <div class="dealer-card" style="left:540px;width:213px">
        <div class="dealer-media">
          <div class="dealer-photo" role="img" aria-label="Dealer portrait" style="width:70px;height:66px"></div>
          <svg class="roadmap" width="135" height="66" viewBox="0 0 135 66"><g stroke="#cfd3e2"><path d="M13.5 0V66M27 0V66M40.5 0V66M54 0V66M67.5 0V66M81 0V66M94.5 0V66M108 0V66M121.5 0V66M0 13H135M0 26H135M0 39H135M0 52H135"/></g><g fill="none" stroke-width="2"><circle cx="7" cy="6.5" r="4.5" stroke="#c8202c"/><circle cx="7" cy="19.5" r="4.5" stroke="#c8202c"/><circle cx="7" cy="32.5" r="4.5" stroke="#2a3fa8"/><circle cx="20" cy="6.5" r="4.5" stroke="#c8202c"/><circle cx="34" cy="6.5" r="4.5" stroke="#2a3fa8"/><circle cx="47" cy="6.5" r="4.5" stroke="#c8202c"/><circle cx="61" cy="6.5" r="4.5" stroke="#c8202c"/></g></svg>
        </div>
        <div class="dealer-meta"><span>Dealer Name</span><span>Deals 999</span></div>
      </div>
      <div class="dealer-card" style="left:760px;width:213px">
        <div class="dealer-media">
          <div class="dealer-photo" role="img" aria-label="Dealer portrait" style="width:70px;height:66px"></div>
          <svg class="roadmap" width="135" height="66" viewBox="0 0 135 66"><g stroke="#cfd3e2"><path d="M13.5 0V66M27 0V66M40.5 0V66M54 0V66M67.5 0V66M81 0V66M94.5 0V66M108 0V66M121.5 0V66M0 13H135M0 26H135M0 39H135M0 52H135"/></g><g fill="none" stroke-width="2"><circle cx="7" cy="6.5" r="4.5" stroke="#c8202c"/><circle cx="20" cy="6.5" r="4.5" stroke="#2a3fa8"/><circle cx="34" cy="6.5" r="4.5" stroke="#c8202c"/><circle cx="47" cy="6.5" r="4.5" stroke="#c8202c"/><circle cx="61" cy="6.5" r="4.5" stroke="#2a3fa8"/><circle cx="74" cy="6.5" r="4.5" stroke="#c8202c"/><circle cx="88" cy="6.5" r="4.5" stroke="#2a3fa8"/><circle cx="88" cy="19.5" r="4.5" stroke="#2a3fa8"/></g></svg>
        </div>
        <div class="dealer-meta"><span>Dealer Name</span><span>Deals 999</span></div>
      </div>
    </div>

    <div class="multiplayer-tab">
      <svg width="16" height="14" viewBox="0 0 16 14"><circle cx="5" cy="4" r="3" fill="#fff"/><circle cx="11" cy="4" r="3" fill="#fff"/><path d="M0 14c0-4 3-6 5-6s5 2 5 6zM6 14c0-4 3-6 5-6s5 2 5 6z" fill="#fff"/></svg>Multiplayer</div>

    <div class="limit-filter">
      <span class="join-any">Join any</span><span></span><span></span><span></span><span></span><span></span>
      <span class="all-limits">ALL Limits</span>
    </div>

    <div class="table-panel">
      <article class="table-card" style="left:7px;top:10px">
        <div class="table-head"><span>Baccarat A5 3C</span><span>Commission 07</span></div>
        <div class="table-head"><span>Bet Limit</span><span>0/100</span></div>
        <div class="join-btn">JOIN</div>
        <div class="felt"><i class="b">B</i><i class="b">B</i><i class="b">B</i><i class="b">B</i><i class="b">B</i><i class="b">B</i><i class="b">B</i><i class="b">B</i><i class="p">P</i><i class="p">P</i><i class="p">P</i><i class="p">P</i><i class="p">P</i><i class="p">P</i><i class="p">P</i><i class="p">P</i></div>
      </article>
      <article class="table-card" style="left:327px;top:10px">
        <div class="table-head"><span>Baccarat A5 3C</span><span>Commission 07</span></div>
        <div class="table-head"><span>Bet Limit</span><span>0/100</span></div>
        <div class="join-btn">JOIN</div>
        <div class="felt"><i class="b">B</i><i class="b">B</i><i class="b">B</i><i class="b">B</i><i class="b">B</i><i class="b">B</i><i class="b">B</i><i class="b">B</i><i class="p">P</i><i class="p">P</i><i class="p">P</i><i class="p">P</i><i class="p">P</i><i class="p">P</i><i class="p">P</i><i class="p">P</i></div>
      </article>
      <article class="table-card" style="left:645px;top:10px">
        <div class="table-head"><span>Baccarat A5 3C</span><span>Commission 07</span></div>
        <div class="table-head"><span>Bet Limit</span><span>0/100</span></div>
        <div class="join-btn">JOIN</div>
        <div class="felt"><i class="b">B</i><i class="b">B</i><i class="b">B</i><i class="b">B</i><i class="b">B</i><i class="b">B</i><i class="b">B</i><i class="b">B</i><i class="p">P</i><i class="p">P</i><i class="p">P</i><i class="p">P</i><i class="p">P</i><i class="p">P</i><i class="p">P</i><i class="p">P</i></div>
      </article>
      <article class="table-card" style="left:7px;top:177px">
        <div class="table-head"><span>Baccarat A5 3C</span><span>Commission 07</span></div>
        <div class="table-head"><span>Bet Limit</span><span>0/100</span></div>
        <div class="join-btn">JOIN</div>
        <div class="felt"><i class="b">B</i><i class="b">B</i><i class="b">B</i><i class="b">B</i><i class="b">B</i><i class="b">B</i><i class="b">B</i><i class="b">B</i><i class="p">P</i><i class="p">P</i><i class="p">P</i><i class="p">P</i><i class="p">P</i><i class="p">P</i><i class="p">P</i><i class="p">P</i></div>
      </article>
      <article class="table-card" style="left:327px;top:177px">
        <div class="table-head"><span>Baccarat A5 3C</span><span>Commission 07</span></div>
        <div class="table-head"><span>Bet Limit</span><span>0/100</span></div>
        <div class="join-btn">JOIN</div>
        <div class="felt"><i class="b">B</i><i class="b">B</i><i class="b">B</i><i class="b">B</i><i class="b">B</i><i class="b">B</i><i class="b">B</i><i class="b">B</i><i class="p">P</i><i class="p">P</i><i class="p">P</i><i class="p">P</i><i class="p">P</i><i class="p">P</i><i class="p">P</i><i class="p">P</i></div>
      </article>
      <article class="table-card" style="left:645px;top:177px">
        <div class="table-head"><span>Baccarat A5 3C</span><span>Commission 07</span></div>
        <div class="table-head"><span>Bet Limit</span><span>0/100</span></div>
        <div class="join-btn">JOIN</div>
        <div class="felt"><i class="b">B</i><i class="b">B</i><i class="b">B</i><i class="b">B</i><i class="b">B</i><i class="b">B</i><i class="b">B</i><i class="b">B</i><i class="p">P</i><i class="p">P</i><i class="p">P</i><i class="p">P</i><i class="p">P</i><i class="p">P</i><i class="p">P</i><i class="p">P</i></div>
      </article>
    </div>
    <div class="scroll-track"><div class="scroll-thumb"></div></div>
  </section>

  <footer class="footer">
    <div class="balance">
      <span class="balance-label">Balance</span>
      <span class="balance-currency">$SGD</span>
      <span class="balance-value">999,999,999</span>
    </div>
  </footer>
</main>
</body>
</html>
```